New business card design needed for Trucking/Staffing company!

I am looking for a business card design. The business name is Harbor Lane Freightworks, LLC. This company is a staffing company for commercial drivers/truck drivers. Most of our customers are trucking/supply companies. Our colors are blue/black/white/grey. The info I have on my current business cards is
-Spot for a name
-2 lines for an address
-3 lines for Office, cell, and fax
-email
-website(currently on backside of card with logo but can go anywhere)
Updates

Project Deadline Extended
Reason: Open to more designs

Target Market(s)

Trucking companies, building supply companies

Industry/Entity Type

Business

Contact Information for Business Card

Edgy but professional

Font styles to use
Other font styles liked:
• Open to suggestions

Colors
0555a3
000000
ffffff
9d9d9d

Requirements
Must have
• Must have the logo incorporated

```html
<!DOCTYPE html>
<html lang="en">
<head>
<meta charset="utf-8">
<title>Harbor Lane Freightworks – Business Card</title>
<link href="https://fonts.googleapis.com/css2?family=Lato:wght@400;700;900&display=swap" rel="stylesheet">
<style>
  :root {
    --bg: #e4e4e4;
    --card: #efefef;
    --navy: #262f8f;
    --ink: #1c1c1c;
    --blue-1: #1a5a9c;
    --blue-2: #1566aa;
    --blue-3: #1f7dbb;
    --blue-4: #2196c4;
    --accent: #1b8fd0;
    --rail: #b9bcbf;
    --rail-light: #cdd0d2;
    --tile-1: #2aa3d8;
    --tile-2: #1e8fcb;
    --tile-3: #1776bd;
    --tile-4: #1460a8;
  }
  * { box-sizing: border-box; margin: 0; padding: 0; }
  html, body {
    width: 1200px; height: 900px; overflow: hidden;
    background: var(--bg);
    font-family: "Lato", Arial, sans-serif;
  }
  .canvas {
    position: relative; width: 1200px; height: 900px;
  }
  .card {
    position: absolute; left: 285px;
    width: 630px; height: 360px;
    background: var(--card);
    box-shadow: 0 6px 18px rgba(0,0,0,0.12);
    overflow: hidden;
  }
  .card--front { top: 70px; }
  .card--back { top: 470px; }

  .band {
    position: absolute; left: 0; width: 100%; height: 46px;
    display: flex;
  }
  .band span { flex: 1; }
  .band--top { top: 0; }
  .band--bottom { bottom: 0; }
  .band--top span:nth-child(1) { background: var(--blue-1); }
  .band--top span:nth-child(2) { background: var(--blue-2); }
  .band--top span:nth-child(3) { background: var(--blue-3); }
  .band--top span:nth-child(4) { background: var(--blue-4); }
  .band--bottom span:nth-child(1) { background: var(--blue-4); }
  .band--bottom span:nth-child(2) { background: var(--blue-3); }
  .band--bottom span:nth-child(3) { background: var(--blue-2); }
  .band--bottom span:nth-child(4) { background: var(--blue-1); }

  .brand {
    position: absolute;
    display: flex; align-items: center; gap: 12px;
    color: var(--navy);
    font-weight: 900;
    text-transform: uppercase;
  }
  .brand__mark {
    width: 14px; height: 14px; background: var(--navy);
  }
  .brand__name { line-height: 1; }
  .brand__name small { display: block; font-size: 0.42em; letter-spacing: 0.18em; text-align: right; margin-top: 6px; }
  .card--front .brand { left: 50%; top: 50%; transform: translate(-50%, -50%); font-size: 44px; letter-spacing: 0.02em; }
  .card--back .brand { left: 42px; top: 148px; font-size: 28px; }

  .rail {
    position: absolute; left: 336px; top: 0; width: 24px; height: 100%;
    background: linear-gradient(180deg, var(--rail-light), var(--rail));
  }
  .tile {
    position: absolute; left: 322px;
    width: 52px; height: 38px; border-radius: 7px;
    display: flex; align-items: center; justify-content: center;
    box-shadow: 0 2px 3px rgba(0,0,0,0.15);
  }
  .tile svg { width: 16px; height: 16px; fill: #fff; }
  .tile--person { top: 92px; background: var(--tile-1); }
  .tile--phone { top: 148px; background: var(--tile-2); }
  .tile--web { top: 204px; background: var(--tile-3); }
  .tile--pin { top: 260px; background: var(--tile-4); }

  .contact {
    position: absolute; left: 400px; top: 82px; width: 220px;
    color: var(--ink); font-size: 15px; line-height: 1.2;
  }
  .contact__name { font-weight: 900; font-size: 19px; letter-spacing: 0.01em; }
  .contact__role { color: var(--accent); font-size: 14px; }
  .contact__group { margin-top: 12px; padding-top: 6px; position: relative; }
  .contact__group::before {
    content: ""; position: absolute; left: 0; top: 0; width: 80px; height: 2px; background: var(--accent);
  }
  .contact__group--first { margin-top: 4px; }
</style>
</head>
<body>
<div class="canvas">

  <section class="card card--front">
    <div class="band band--top"><span></span><span></span><span></span><span></span></div>
    <div class="brand">
      <span class="brand__mark"></span>
      <span class="brand__name">Harbor Lane<small>Freightworks</small></span>
    </div>
    <div class="band band--bottom"><span></span><span></span><span></span><span></span></div>
  </section>

  <section class="card card--back">
    <div class="brand">
      <span class="brand__mark"></span>
      <span class="brand__name">Harbor Lane<small>Freightworks</small></span>
    </div>

    <div class="rail"></div>
    <div class="tile tile--person">
      <svg viewBox="0 0 16 16"><circle cx="8" cy="4.5" r="3"/><path d="M2.5 15c0-3.5 2.5-6 5.5-6s5.5 2.5 5.5 6z"/></svg>
    </div>
    <div class="tile tile--phone">
      <svg viewBox="0 0 16 16"><path d="M3.6 1.5l2.3 2.6-1.3 1.9c.9 2 2.5 3.6 4.5 4.5l1.9-1.3 2.6 2.3-1.2 2.4C7.3 13.7 2.3 8.7 1.2 3.1z"/></svg>
    </div>
    <div class="tile tile--web">
      <svg viewBox="0 0 16 16"><path d="M8 1a7 7 0 1 0 0 14A7 7 0 0 0 8 1zm0 1.6c.9 1 1.5 2.5 1.7 4.6H6.3C6.5 5.1 7.1 3.6 8 2.6zM6.3 8.8h3.4c-.2 2.1-.8 3.6-1.7 4.6-.9-1-1.5-2.5-1.7-4.6zM2.7 7.2a5.4 5.4 0 0 1 2.6-4c-.4 1.1-.6 2.5-.7 4zm0 1.6h1.9c.1 1.5.3 2.9.7 4a5.4 5.4 0 0 1-2.6-4zm8.7 0h1.9a5.4 5.4 0 0 1-2.6 4c.4-1.1.6-2.5.7-4zm0-1.6c-.1-1.5-.3-2.9-.7-4a5.4 5.4 0 0 1 2.6 4z"/></svg>
    </div>
    <div class="tile tile--pin">
      <svg viewBox="0 0 16 16"><path d="M8 1a5 5 0 0 0-5 5c0 3.8 5 9 5 9s5-5.2 5-9a5 5 0 0 0-5-5zm0 7a2 2 0 1 1 0-4 2 2 0 0 1 0 4z"/></svg>
    </div>

    <div class="contact">
      <p class="contact__name">JOHN SMITH</p>
      <p class="contact__role">CEO DIRECTOR</p>
      <div class="contact__group contact__group--first">
        <p>+000 898 5845</p>
        <p>+000 554 8888</p>
      </div>
      <div class="contact__group">
        <p>urname@email.com</p>
        <p>urwebsite.com</p>
      </div>
      <div class="contact__group">
        <p>ur address goes here</p>
        <p>street, zip code 9840</p>
      </div>
    </div>
  </section>

</div>
</body>
</html>
```